Showroom Quote Web Application - Material Design wanted

This web app is an internal application that will be used by one of our customers to build quotes and produce orders of retail items with their customers

the overall design should use the colour pallet provided and have a clean and simple interface

we'd like to go with a material design type of look

attached mockups are just a rough stab at some layouts to give you an example, please feel free to reach out with any questions.

Please don't get hung up on the specific pages, they were intended to provide context, we are looking for a high level design using the provided colour schemes and fonts, additional work may follow for the selected designer when it comes to specific pages or work flows.

Sorry for the short timeline, we have a tight deadline on this one.

Target Market(s)

internal application for customer

Industry/Entity Type

Retail

Other font styles liked:
• see attached doc for fonts

Requirements
Must have
• simple and clean interface
• intuitive design
Nice to have
• see attached documents for logo colour schemes and fonts
• these must be incorporated into the design

```html
<!DOCTYPE html>
<html lang="en">
<head>
<meta charset="utf-8">
<title>Plumbing Showroom Quote System</title>
<link href="https://fonts.googleapis.com/css2?family=Roboto:wght@400;500&display=swap" rel="stylesheet">
<style>
  :root{
    --page-bg:#eceef1;
    --navy:#1b3f7d;
    --action-blue:#2b70cc;
    --gold:#b8985a;
    --gold-dark:#a98a4e;
    --ink:#1f1f1f;
    --muted:#8a8a8a;
    --link:#3a84e2;
    --row-alt:#f1f1f1;
    --row:#ffffff;
    --rule:#dcdcdc;
  }
  *{box-sizing:border-box;margin:0;padding:0}
  html,body{width:1200px;height:884px;overflow:hidden}
  body{background:var(--page-bg);font-family:"Roboto",Arial,sans-serif;color:var(--ink);position:relative}
  .app-title{position:absolute;top:120px;left:0;width:1200px;text-align:center;font-size:28px;font-weight:400;color:#2b2b2b}
  .quote-panel{position:absolute;top:190px;left:83px;width:1034px;box-shadow:0 2px 6px rgba(0,0,0,.18)}
  .toolbar{background:var(--navy);height:66px;display:flex;align-items:center;padding:0 10px;gap:9px}
  .search-field{flex:0 0 612px;height:46px;background:#fff;border-radius:2px;display:flex;align-items:center;padding:0 12px;gap:12px;color:var(--muted);font-size:18px}
  .status-select{flex:0 0 248px;height:46px;background:#fff;border-radius:2px;display:flex;align-items:center;justify-content:space-between;padding:0 12px 0 10px;font-size:18px;color:var(--ink)}
  .filter-button{flex:1;height:46px;background:var(--action-blue);color:#fff;border:none;font:400 18px "Roboto",Arial,sans-serif;border-radius:2px}
  .quote-table{width:100%;border-collapse:collapse;table-layout:fixed;font-size:18px}
  .quote-table th{background:var(--gold);color:#fff;font-weight:400;font-size:16px;height:34px;text-align:left;padding:0 10px;border-right:1px solid var(--gold-dark)}
  .quote-table th:last-child{border-right:none;text-align:center}
  .th-inner{display:flex;justify-content:space-between;align-items:center}
  .quote-table td{height:49px;padding:0 10px;border-right:1px solid var(--rule);border-bottom:1px solid var(--rule);background:var(--row)}
  .quote-table td:last-child{border-right:none;text-align:center}
  .quote-table tr:nth-child(even) td{background:var(--row-alt)}
  .edit-link{color:var(--link);text-decoration:none;display:inline-flex;align-items:center;gap:6px}
  .add-quote{position:absolute;right:12px;bottom:14px;width:54px;height:54px;border-radius:50%;background:var(--gold);box-shadow:0 2px 5px rgba(0,0,0,.3);display:flex;align-items:center;justify-content:center}
</style>
</head>
<body>
  <h1 class="app-title">Plumbing Showroom Quote System (PSQS)</h1>
  <section class="quote-panel">
    <div class="toolbar">
      <div class="search-field">
        <svg width="20" height="20" viewBox="0 0 20 20"><circle cx="8" cy="8" r="6.5" fill="none" stroke="#777" stroke-width="1.6"/><line x1="13" y1="13" x2="18.5" y2="18.5" stroke="#777" stroke-width="1.6"/></svg>
        <span>search by quote # or customer name</span>
      </div>
      <div class="status-select"><span>Open</span><svg width="14" height="8" viewBox="0 0 14 8"><path d="M0 0h14L7 7z" fill="#666"/></svg></div>
      <button class="filter-button">Filter</button>
    </div>
    <table class="quote-table">
      <colgroup><col style="width:152px"><col style="width:252px"><col style="width:152px"><col style="width:152px"><col style="width:229px"><col style="width:97px"></colgroup>
      <thead>
        <tr>
          <th><span class="th-inner">Quote #<svg width="9" height="14" viewBox="0 0 9 14"><path d="M4.5 0L9 5H0zM4.5 14L0 9h9z" fill="#1b3f7d"/></svg></span></th>
          <th><span class="th-inner">Customer<svg width="9" height="14" viewBox="0 0 9 14"><path d="M4.5 0L9 5H0zM4.5 14L0 9h9z" fill="#1b3f7d"/></svg></span></th>
          <th><span class="th-inner">Date<svg width="9" height="14" viewBox="0 0 9 14"><path d="M4.5 0L9 5H0zM4.5 14L0 9h9z" fill="#1b3f7d"/></svg></span></th>
          <th><span class="th-inner">Vallue<svg width="9" height="14" viewBox="0 0 9 14"><path d="M4.5 0L9 5H0zM4.5 14L0 9h9z" fill="#1b3f7d"/></svg></span></th>
          <th><span class="th-inner">Description<svg width="9" height="14" viewBox="0 0 9 14"><path d="M4.5 0L9 5H0zM4.5 14L0 9h9z" fill="#1b3f7d"/></svg></span></th>
          <th>Action</th>
        </tr>
      </thead>
      <tbody>
        <tr><td>1234</td><td>Marco Bellandi</td><td>2017-09-30</td><td>$5,300.0</td><td>New House</td><td><a class="edit-link" href="#">edite <svg width="13" height="13" viewBox="0 0 13 13"><path d="M0 13l1-4 8-8 3 3-8 8z" fill="#3a84e2"/></svg></a></td></tr>
        <tr><td>1235</td><td>Arlen Watts</td><td>2017-10-01</td><td>$4,200.0</td><td>Old House</td><td><a class="edit-link" href="#">edite <svg width="13" height="13" viewBox="0 0 13 13"><path d="M0 13l1-4 8-8 3 3-8 8z" fill="#3a84e2"/></svg></a></td></tr>
        <tr><td>1236</td><td>Fen Sorrell</td><td>2017-10-03</td><td>$3,100.0</td><td>New House</td><td><a class="edit-link" href="#">edite <svg width="13" height="13" viewBox="0 0 13 13"><path d="M0 13l1-4 8-8 3 3-8 8z" fill="#3a84e2"/></svg></a></td></tr>
        <tr><td>1237</td><td>Lin Archer</td><td>2017-10-03</td><td>$6,400.0</td><td>New House</td><td><a class="edit-link" href="#">edite <svg width="13" height="13" viewBox="0 0 13 13"><path d="M0 13l1-4 8-8 3 3-8 8z" fill="#3a84e2"/></svg></a></td></tr>
        <tr><td>1238</td><td>Avery O-dell</td><td>2017-10-04</td><td>$2,200.0</td><td>Old House</td><td><a class="edit-link" href="#">edite <svg width="13" height="13" viewBox="0 0 13 13"><path d="M0 13l1-4 8-8 3 3-8 8z" fill="#3a84e2"/></svg></a></td></tr>
        <tr><td>1239</td><td>Sela Marsh</td><td>2017-10-04</td><td>$2,500.0</td><td>Old House</td><td><a class="edit-link" href="#">edite <svg width="13" height="13" viewBox="0 0 13 13"><path d="M0 13l1-4 8-8 3 3-8 8z" fill="#3a84e2"/></svg></a></td></tr>
        <tr><td></td><td></td><td></td><td></td><td></td><td></td></tr>
        <tr><td></td><td></td><td></td><td></td><td></td><td></td></tr>
      </tbody>
    </table>
    <div class="add-quote" aria-label="Add quote">
      <svg width="20" height="20" viewBox="0 0 20 20"><path d="M10 2v16M2 10h16" stroke="#fff" stroke-width="2"/></svg>
    </div>
  </section>
</body>
</html>
```